Willow Glow & Laser - Business Banner with Brand Elements

Design:
• We would like to get a creative design for a wide banner that will go outside our medical spa clinic location. We need a designer to make a simple yet colorful and high-quality design layout. We want this banner to be eye-catching and to communicate the services we offer at our business: Laser Hair Removal | Velonix | Lip Filler.

Requirements:
• We would like the banner to include our companies information which is the following:

Logo
“Refresh Your Skin”
Laser Hair Removal | Velonix | Lip Filler
(555) 287-1936
www.WillowGlowLaser.com

Colors:
• Our business colors are orange, a hint of black and white, but mostly peach/orange tones. (Orange: #f78f20 , White: #ffffff)

Fonts:
• Josefins Sans Bold & Lato

Content and images can be located here:
https://files.cloudvaultshare.com/folders/7tQmZ2xVbR9kLpN4sW8yH3cD6fJ1gA0eU?usp=sharing

The following will give you an idea of our brand presentation:
• Our website is: www.WillowGlowLaser.com
• Our Instagram; @willowglowlaser
• Our Facebook: www.socialpagehub.com/willowglowlaser

Target Market(s)
• Women 25 - 45

Industry/Entity Type
• Beauty

```html
<!DOCTYPE html>
<html lang="en">
<head>
<meta charset="utf-8">
<title>Willow Glow &amp; Laser – Banners</title>
<link rel="stylesheet" href="https://fonts.googleapis.com/css2?family=Josefin+Sans:wght@600;700&family=Roboto:wght@400;500;700&display=swap">
<style>
:root{
  --board:#efefef;
  --orange:#f6a444;
  --white:#ffffff;
  --ink:#111111;
  --sky:#8fd3ea;
  --sea:#3fc3da;
  --sand:#f2e2d4;
}
*{margin:0;padding:0;box-sizing:border-box}
html,body{width:1109px;height:1200px;overflow:hidden;background:var(--board)}
.board{position:relative;width:1109px;height:1200px}
.banner{position:absolute;left:69px;width:970px;height:485px;overflow:hidden}
.banner--light{top:78px;background:#fbfbfb}
.banner--orange{top:638px;background:var(--board)}

.faded-scene{position:absolute;inset:0;background:
  radial-gradient(ellipse 170px 210px at 310px 190px,rgba(235,222,214,.55),rgba(235,222,214,0) 70%),
  radial-gradient(ellipse 150px 200px at 500px 150px,rgba(235,222,214,.5),rgba(235,222,214,0) 70%),
  #fbfaf9}
.hero-shape{position:absolute;inset:0}

.brand-box{position:absolute;left:78px;top:76px;width:108px;height:108px;background:var(--white);display:flex;flex-direction:column;align-items:center;justify-content:center;gap:6px}
.brand-dot{width:22px;height:22px;border-radius:50%;background:var(--orange)}
.brand-name{font-family:'Josefin Sans',sans-serif;font-weight:700;font-size:15px;line-height:1.05;text-align:center;color:var(--ink)}
.brand-name--light{color:var(--white);font-size:22px;text-align:left}

.headline{position:absolute;font-family:'Josefin Sans',sans-serif;font-weight:700;font-size:33px;letter-spacing:.5px;white-space:nowrap}
.banner--light .headline{left:89px;top:210px;color:var(--orange)}

.service-list{position:absolute;left:89px;top:260px;list-style:none}
.service-list li{display:flex;align-items:center;gap:18px;height:28.5px;font-family:'Josefin Sans',sans-serif;font-weight:600;font-size:14.5px;letter-spacing:.6px;color:var(--ink)}
.service-list svg{width:12px;height:12px}

.contact{position:absolute;display:flex;align-items:center;font-family:'Roboto',sans-serif}
.contact-badge{width:38px;height:38px;border-radius:50%;background:var(--orange);display:flex;align-items:center;justify-content:center}
.contact-badge svg{width:17px;height:17px}
.contact-label{font-weight:500;font-size:10px;color:var(--ink);text-transform:uppercase}
.contact-phone{font-weight:500;font-size:17.5px;color:var(--orange)}
.contact-web{font-size:11.5px;color:var(--orange)}
.contact--call{left:89px;top:371px}
.contact--email{left:299px;top:371px}
.contact--call .contact-text{margin-left:30px;margin-top:-6px}
.contact--email .contact-text{margin-left:30px}

.orange-panel{position:absolute;left:0;top:0;width:508px;height:485px;background:
  radial-gradient(ellipse 150px 230px at 330px 270px,rgba(240,150,60,.35),rgba(240,150,60,0) 70%),
  var(--orange)}
.orange-panel .brand{position:absolute;left:89px;top:82px;display:flex;flex-direction:column;gap:10px}
.brand-dot--light{background:var(--white);width:30px;height:30px}
.banner--orange .headline{left:89px;top:202px;color:var(--white)}
.icon-row{position:absolute;top:274px;left:0;width:508px}
.icon-item{position:absolute;width:140px;margin-left:-70px;text-align:center}
.icon-ring{width:48px;height:48px;margin:0 auto;border:2px solid var(--white);border-radius:50%;display:flex;align-items:center;justify-content:center}
.icon-ring svg{width:28px;height:28px}
.icon-label{margin-top:14px;font-family:'Roboto',sans-serif;font-weight:700;font-size:11px;color:var(--white)}
.panel-contact{position:absolute;top:386px;display:flex;align-items:center;gap:12px;font-family:'Roboto',sans-serif;color:var(--white)}
.panel-contact svg{width:15px;height:15px}
.panel-contact--call{left:100px;font-weight:500;font-size:17.5px}
.panel-contact--web{left:295px;font-size:11.5px}
.beach-scene{position:absolute;left:519px;top:0;width:451px;height:485px;background:
  linear-gradient(180deg,#e4ecf3 0%,#cddff0 18%,#b9d3ea 23%,#21b9d6 23.6%,#36c3dc 38%,#6fd2e0 55%,#b8e2e0 64%,#ecdcd0 70%,#f3e2d6 100%)}
</style>
</head>
<body>
<main class="board">

  <section class="banner banner--light">
    <div class="faded-scene" role="img" aria-label="Faded photo of two smiling women with glowing skin"></div>
    <svg class="hero-shape" viewBox="0 0 970 485" width="970" height="485">
      <defs>
        <linearGradient id="beachGlow" x1="0" y1="0" x2="0" y2="1">
          <stop offset="0" stop-color="#6fcbe6"/>
          <stop offset="0.34" stop-color="#a9dcea"/>
          <stop offset="0.36" stop-color="#5fc2d2"/>
          <stop offset="0.5" stop-color="#9fd8de"/>
          <stop offset="0.64" stop-color="#d9e6e4"/>
          <stop offset="0.7" stop-color="#ecdfd2"/>
          <stop offset="1" stop-color="#f3e5d8"/>
        </linearGradient>
      </defs>
      <polygon points="583,51 483,241 580,428 516,241" fill="#f6a444"/>
      <polygon points="602,0 970,0 970,485 602,485 510,241" fill="url(#beachGlow)" role="img" aria-label="Photo of a smiling woman in a striped swimsuit on a sunny beach"/>
    </svg>

    <div class="brand-box">
      <span class="brand-dot"></span>
      <span class="brand-name">Willow Glow<br>&amp; Laser</span>
    </div>

    <h1 class="headline">REFRESH YOUR SKIN</h1>
    <ul class="service-list">
      <li><svg viewBox="0 0 12 12"><circle cx="6" cy="6" r="6" fill="#f6a444"/><path d="M3 6h5M6 3.5 8.5 6 6 8.5" stroke="#fff" stroke-width="1.5" fill="none"/></svg>LASER HAIR REMOVAL</li>
      <li><svg viewBox="0 0 12 12"><circle cx="6" cy="6" r="6" fill="#f6a444"/><path d="M3 6h5M6 3.5 8.5 6 6 8.5" stroke="#fff" stroke-width="1.5" fill="none"/></svg>VELONIX</li>
      <li><svg viewBox="0 0 12 12"><circle cx="6" cy="6" r="6" fill="#f6a444"/><path d="M3 6h5M6 3.5 8.5 6 6 8.5" stroke="#fff" stroke-width="1.5" fill="none"/></svg>LIP FILLER</li>
    </ul>

    <div class="contact contact--call">
      <span class="contact-badge"><svg viewBox="0 0 24 24"><path fill="#fff" d="M6.6 10.8a15.1 15.1 0 0 0 6.6 6.6l2.2-2.2c.3-.3.7-.4 1-.2 1.1.4 2.3.6 3.6.6.6 0 1 .4 1 1V20c0 .6-.4 1-1 1A17 17 0 0 1 3 4c0-.6.4-1 1-1h3.5c.6 0 1 .4 1 1 0 1.3.2 2.5.6 3.6.1.3 0 .7-.2 1z"/></svg></span>
      <div class="contact-text"><div class="contact-label">Call us</div><div class="contact-phone">(555) 287-1936</div></div>
    </div>
    <div class="contact contact--email">
      <span class="contact-badge"><svg viewBox="0 0 24 24"><path fill="#fff" d="M3 6h18v2l-9 5.5L3 8zm0 4.3 9 5.5 9-5.5V18H3z"/></svg></span>
      <div class="contact-text"><div class="contact-label">Email us</div><div class="contact-web">www.WillowGlowLaser.com</div></div>
    </div>
  </section>

  <section class="banner banner--orange">
    <div class="orange-panel">
      <div class="brand">
        <span class="brand-dot brand-dot--light"></span>
        <span class="brand-name brand-name--light">Willow Glow<br>&amp; Laser</span>
      </div>
      <h2 class="headline">REFRESH YOUR SKIN</h2>
      <div class="icon-row">
        <div class="icon-item" style="left:154px">
          <div class="icon-ring"><svg viewBox="0 0 28 28" fill="none" stroke="#fff" stroke-width="1.5" stroke-linecap="round"><rect x="5" y="15" width="18" height="7" rx="1.5"/><path d="M8 15v-3h6v3M11 12V8M9 5l2 3 2-3M17 8l2-2M18 11h3M8 19h2M13 19h2M18 19h2"/></svg></div>
          <div class="icon-label">LASER HAIR REMOVAL</div>
        </div>
        <div class="icon-item" style="left:285px">
          <div class="icon-ring"><svg viewBox="0 0 28 28" fill="none" stroke="#fff" stroke-width="1.5" stroke-linecap="round"><path d="M19 5l4 4M21 7l-3 3M18 8l-9 9 2 2 9-9zM9 17l-4 4M13 11l2 2M11 13l2 2"/></svg></div>
          <div class="icon-label">VELONIX</div>
        </div>
        <div class="icon-item" style="left:417px">
          <div class="icon-ring"><svg viewBox="0 0 28 28" fill="none" stroke="#fff" stroke-width="1.5" stroke-linecap="round" stroke-linejoin="round"><path d="M14 10c-3 4-5 6-5 9a5 5 0 0 0 10 0c0-3-2-5-5-9z"/><path d="M8 9V4M6 6l2-2 2 2M20 9V4M18 6l2-2 2 2"/></svg></div>
          <div class="icon-label">LIP FILLER</div>
        </div>
      </div>
      <div class="panel-contact panel-contact--call">
        <svg viewBox="0 0 24 24"><path fill="#fff" d="M6.6 10.8a15.1 15.1 0 0 0 6.6 6.6l2.2-2.2c.3-.3.7-.4 1-.2 1.1.4 2.3.6 3.6.6.6 0 1 .4 1 1V20c0 .6-.4 1-1 1A17 17 0 0 1 3 4c0-.6.4-1 1-1h3.5c.6 0 1 .4 1 1 0 1.3.2 2.5.6 3.6.1.3 0 .7-.2 1z"/></svg>
        <span>(555) 287-1936</span>
      </div>
      <div class="panel-contact panel-contact--web">
        <svg viewBox="0 0 24 24"><path fill="#fff" d="M3 5h18v2.5l-9 5.5-9-5.5zm0 4.8 9 5.5 9-5.5V19H3z"/></svg>
        <span>www.WillowGlowLaser.com</span>
      </div>
    </div>
    <div class="beach-scene" role="img" aria-label="Photo of a smiling woman lying on the sand by a turquoise sea"></div>
  </section>

</main>
</body>
</html>
```